Business Card, Etc.
Bcard, Stationary and Envelope
Business Card, Etc.  - Consulting
Creative Brief
Professional
Marcus D. Fenwick
President
784 Maple Ave West Brookfield, NE 50814-2391
marcus.fenwick@tvbadvisory.com
www.tvbadvisory.com
The logo uses BankGothicBT Medium. You do not have to match the font in the logo. We might like to see a completing font. We are also going to want trading cards and a PowerPoint template when this is done!

```html
<!DOCTYPE html>
<html lang="en">
<head>
<meta charset="utf-8">
<title>TVB Advisory Business Card</title>
<link rel="stylesheet" href="https://fonts.googleapis.com/css2?family=Open+Sans:wght@400;600;700&display=swap">
<style>
:root{
  --navy:#1d4a6c;
  --navy-deep:#143a57;
  --paper:#ffffff;
  --stripe:#c9ced3;
  --ink:#1d4a6c;
  --bg:#8a8c8f;
}
*{box-sizing:border-box;margin:0;padding:0}
html,body{width:1200px;height:908px;overflow:hidden}
body{background:var(--bg);font-family:"Open Sans",Arial,sans-serif}
.canvas{position:relative;width:1200px;height:908px}
.card{position:absolute;width:560px;height:320px;border-radius:22px;overflow:hidden;box-shadow:0 10px 28px rgba(0,0,0,.28)}
.card-front{left:80px;top:110px;background:linear-gradient(150deg,#25587d 0%,var(--navy) 45%,var(--navy-deep) 100%);display:flex;align-items:center;justify-content:center}
.card-back{left:560px;top:478px;background:var(--paper)}
.brand{display:flex;align-items:center;gap:14px;font-weight:700;letter-spacing:.12em;text-transform:uppercase;white-space:nowrap}
.brand-mark{width:30px;height:30px;flex:none}
.card-front .brand{color:var(--paper);font-size:34px}
.card-front .brand-mark{background:var(--paper)}
.card-back .brand{position:absolute;left:34px;top:76px;color:var(--ink);font-size:24px}
.card-back .brand-mark{background:var(--ink);width:24px;height:24px}
.back-stripe{position:absolute;left:0;right:0;top:196px;height:8px;background:var(--stripe)}
.back-band{position:absolute;left:0;right:0;top:204px;bottom:0;background:var(--navy)}
.person{position:absolute;left:34px;top:30px;color:var(--paper)}
.person-name{font-size:20px;font-weight:600}
.person-title{font-size:14px;margin-top:2px}
.contacts{position:absolute;left:300px;top:26px;list-style:none;color:var(--ink);font-size:11.5px;line-height:1}
.contacts li{display:flex;align-items:center;gap:8px;height:19px;white-space:nowrap}
.icon{width:13px;height:13px;flex:none}
</style>
</head>
<body>
<main class="canvas">
  <section class="card card-front" aria-label="Card front">
    <div class="brand"><span class="brand-mark"></span>TVB Advisory</div>
  </section>

  <section class="card card-back" aria-label="Card back">
    <div class="brand"><span class="brand-mark"></span>TVB Advisory</div>

    <ul class="contacts">
      <li>784 Maple Ave West</li>
      <li>Brookfield, NE 50814-2391</li>
      <li><svg class="icon" viewBox="0 0 14 14"><circle cx="7" cy="7" r="7" fill="#1d4a6c"/><path d="M4.5 3.5l1.5 0 .6 1.8-.9.7a5 5 0 002.3 2.3l.7-.9 1.8.6v1.5c-3.5.3-6.5-2.7-6-6z" fill="#fff"/></svg>800-555-0170 (Toll Free)</li>
      <li><svg class="icon" viewBox="0 0 14 14"><circle cx="7" cy="7" r="7" fill="#1d4a6c"/><path d="M4.5 3.5l1.5 0 .6 1.8-.9.7a5 5 0 002.3 2.3l.7-.9 1.8.6v1.5c-3.5.3-6.5-2.7-6-6z" fill="#fff"/></svg>402-555-0142</li>
      <li><svg class="icon" viewBox="0 0 14 14"><circle cx="7" cy="7" r="7" fill="#1d4a6c"/><path d="M4.5 3.5l1.5 0 .6 1.8-.9.7a5 5 0 002.3 2.3l.7-.9 1.8.6v1.5c-3.5.3-6.5-2.7-6-6z" fill="#fff"/></svg>402-555-0187</li>
      <li><svg class="icon" viewBox="0 0 14 14"><circle cx="7" cy="7" r="7" fill="#1d4a6c"/><rect x="3.5" y="4" width="7" height="6" fill="#fff"/><rect x="5" y="2.8" width="4" height="1.6" fill="#fff"/></svg>402-555-0163</li>
      <li><svg class="icon" viewBox="0 0 14 14"><circle cx="7" cy="7" r="7" fill="#1d4a6c"/><rect x="3.5" y="4.5" width="7" height="5" fill="#fff"/><path d="M3.5 4.5l3.5 3 3.5-3" fill="none" stroke="#1d4a6c" stroke-width=".8"/></svg>marcus.fenwick@tvbadvisory.com</li>
      <li><svg class="icon" viewBox="0 0 14 14"><circle cx="7" cy="7" r="7" fill="#1d4a6c"/><circle cx="7" cy="7" r="3.6" fill="none" stroke="#fff" stroke-width=".9"/><path d="M3.4 7h7.2M7 3.4v7.2" stroke="#fff" stroke-width=".8"/></svg>www.tvbadvisory.com</li>
    </ul>

    <div class="back-stripe"></div>
    <div class="back-band">
      <div class="person">
        <p class="person-name">Marcus D. Fenwick</p>
        <p class="person-title">President</p>
      </div>
    </div>
  </section>
</main>
</body>
</html>
```